Business Card Design Project

We are a distribution company providing goods to Latin America. We sell everything from Medical equipment, generic medicines, to carecliners. The logo that we use is attached. The logo can incorporate different colors other than black for versatility. The company name is Valdren Global Enterprises and/or VGE. The card will be printed using 1 or more of the following: Silk mounted and/or embossed. So if the design ideas could be made to incorporate that technique or any other unique techniques, it would be great. The target market is dialysis centers/doctors.

Basic Info for card:
Marna Dowell
Purchasing Manager
417-305-6184 direct
417-521-7790 fax
marna.dowell@valdrenvge.example
www.valdrenvge.example

Target Market(s)

Latin America

Industry/Entity Type

Business

Requirements
Nice to have
• The Front of the card should have the basic contact information with company name/logo. The back of the card could incorporate

```html
<!DOCTYPE html>
<html lang="en">
<head>
<meta charset="utf-8">
<title>Valdren Global Enterprises – Business Card</title>
<link href="https://fonts.googleapis.com/css2?family=Open+Sans:wght@400;600;700&display=swap" rel="stylesheet">
<style>
  :root {
    --backdrop: #e9e4dc;
    --card-black: #1a1a1a;
    --card-black-light: #2c2c2c;
    --brand-red: #f01414;
    --swoosh-grey: #7a7a7a;
    --text-white: #f4f4f4;
    --divider: #8a8a8a;
  }
  * { box-sizing: border-box; margin: 0; padding: 0; }
  html, body { width: 1200px; height: 1117px; overflow: hidden; }
  body {
    background: var(--backdrop);
    font-family: "Open Sans", Arial, sans-serif;
    position: relative;
  }
  .card {
    position: absolute;
    width: 760px;
    height: 434px;
    background: radial-gradient(ellipse at 60% 40%, var(--card-black-light), var(--card-black) 70%);
    overflow: hidden;
    box-shadow: 0 10px 28px rgba(0,0,0,.35);
  }
  .card--front { left: 50px; top: 70px; }
  .card--back { left: 390px; top: 610px; }

  .brand {
    position: absolute;
    display: flex;
    align-items: center;
    gap: 18px;
    color: var(--text-white);
    font-weight: 400;
  }
  .brand__dot {
    border-radius: 50%;
    background: var(--brand-red);
    flex: none;
  }
  .card--front .brand { left: 70px; top: 150px; font-size: 60px; letter-spacing: 16px; }
  .card--front .brand__dot { width: 46px; height: 46px; }

  .divider {
    position: absolute;
    left: 380px; top: 70px;
    width: 2px; height: 270px;
    background: var(--divider);
  }
  .contact { position: absolute; left: 410px; top: 92px; color: var(--text-white); }
  .contact__name { color: var(--brand-red); font-weight: 700; font-size: 22px; }
  .contact__title { font-size: 23px; margin-top: 2px; }
  .contact__list { list-style: none; margin-top: 30px; font-size: 18.5px; line-height: 29px; }
  .contact__list li { display: flex; align-items: center; gap: 10px; }
  .contact__list svg { width: 16px; height: 16px; fill: var(--text-white); flex: none; }

  .swoosh { position: absolute; left: 0; bottom: 0; width: 760px; height: 180px; }

  .card--back .brand { left: 0; right: 0; top: 120px; justify-content: center; font-size: 96px; letter-spacing: 22px; }
  .card--back .brand__dot { width: 70px; height: 70px; }
  .back__url {
    position: absolute; left: 0; right: 0; top: 318px;
    text-align: center; color: var(--text-white);
    font-size: 30px; letter-spacing: 7px;
  }
</style>
</head>
<body>
  <section class="card card--front" aria-label="Card front">
    <div class="brand"><span class="brand__dot"></span><span class="brand__name">VGE</span></div>
    <div class="divider"></div>
    <div class="contact">
      <p class="contact__name">Marna Dowell</p>
      <p class="contact__title">Purchasing Manager</p>
      <ul class="contact__list">
        <li><svg viewBox="0 0 16 16"><circle cx="8" cy="8" r="7.5" fill="none" stroke="#f4f4f4" stroke-width="1.2"/><path d="M5 4.5c.6-.6 1.2-.4 1.5.2l.6 1.2c.2.4 0 .8-.3 1l-.4.3c.5 1 1.2 1.8 2.2 2.3l.3-.4c.3-.3.7-.4 1-.2l1.2.6c.6.3.7 1 .2 1.5-1.4 1.4-4 .2-5.5-1.4C4.6 8.2 3.7 5.8 5 4.5z"/></svg>417-305-6184</li>
        <li><svg viewBox="0 0 16 16"><rect x="4" y="2" width="8" height="5"/><rect x="1" y="7" width="14" height="6" rx="1"/><rect x="4" y="11" width="8" height="3" fill="#1a1a1a"/></svg>417-521-7790</li>
        <li><svg viewBox="0 0 16 16"><path d="M1 5l7-4 7 4v9H1z"/><path d="M1 5l7 5 7-5" fill="none" stroke="#1a1a1a" stroke-width="1.2"/></svg>marna.dowell@valdrenvge.example</li>
        <li><svg viewBox="0 0 16 16"><circle cx="8" cy="8" r="7" fill="none" stroke="#f4f4f4" stroke-width="1.2"/><ellipse cx="8" cy="8" rx="3" ry="7" fill="none" stroke="#f4f4f4" stroke-width="1"/><path d="M1 8h14M2.5 4.5h11M2.5 11.5h11" stroke="#f4f4f4" stroke-width="1"/></svg>www.valdrenvge.example</li>
      </ul>
    </div>
    <svg class="swoosh" viewBox="0 0 760 180" preserveAspectRatio="none">
      <path d="M0 180V150C180 80 420 120 760 40V180Z" fill="var(--brand-red)"/>
      <path d="M0 150C160 90 420 110 760 40V55C440 130 180 110 0 160Z" fill="var(--card-black)"/>
      <path d="M0 140C180 80 430 95 760 25V40C430 105 170 100 0 150Z" fill="var(--swoosh-grey)"/>
    </svg>
  </section>

  <section class="card card--back" aria-label="Card back">
    <div class="brand"><span class="brand__dot"></span><span class="brand__name">VGE</span></div>
    <p class="back__url">www.valdrenvge.example</p>
  </section>
</body>
</html>
```